Willowmere Counseling (Endure - Mend - Flourish) - Double Sided Business Card

I would like a 2-sided business card. Front: Matte Black or Navy with Logo & Tagline. Back: Name, Address, Phone Number, Email, & Website (maybe would like to include a small map pin-pointing location); Prefer front to be a gold/silver foil (iridescent); Back prefer white or light colored background with lettering that is easy to read and simple

Target Market(s)

Individuals & Couples (13 y.o. - ALL Adults); High end clientele

Industry/Entity Type

Licensed Professional Counselor (Mental Health)

Contact Information for Business Card

Name: Willowmere Counseling; Tagline: Endure - Mend - Flourish; Address: 3870 N. Garrick Ave., Suite 214, Fort Worth, TX 76132; Phone: (214) 555-0187; Website: www.WillowmereCounseling.example

Font styles to use
Serif

Requirements
Must have
• Logo on Front (Large) prefer gold/silver foil on a matte dark color (i.e. black, navy, etc.); Back of Card: All other relevant information

```html
<!DOCTYPE html>
<html lang="en">
<head>
<meta charset="utf-8">
<title>Willowmere Counseling – Business Card</title>
<link rel="stylesheet" href="https://fonts.googleapis.com/css2?family=Cinzel:wght@400;600&display=swap">
<style>
  :root {
    --backdrop: #2b2b2b;
    --card-dark: #222222;
    --card-light: #ffffff;
    --gold: #c9a94a;
    --gold-foil: #d4ad3c;
    --slate: #6f6f71;
  }
  * { margin: 0; padding: 0; box-sizing: border-box; }
  html, body { width: 1200px; height: 900px; overflow: hidden; }
  body {
    background: var(--backdrop);
    font-family: "Cinzel", serif;
    display: flex;
    flex-direction: column;
    align-items: center;
    justify-content: center;
    gap: 36px;
  }
  .card {
    width: 700px;
    height: 400px;
    position: relative;
    display: flex;
    flex-direction: column;
    align-items: center;
    box-shadow: 0 14px 30px rgba(0,0,0,.45);
  }
  .card--front { background: var(--card-dark); justify-content: center; color: var(--gold-foil); }
  .card--back { background: var(--card-light); padding-top: 46px; color: var(--gold); }
  .brand-mark {
    width: 74px; height: 74px; border-radius: 50%;
    background: currentColor; margin-bottom: 18px;
  }
  .card--back .brand-mark { width: 62px; height: 62px; margin-bottom: 14px; }
  .brand-name {
    font-weight: 600; font-size: 44px; letter-spacing: 2px;
    text-transform: uppercase; line-height: 1.05; text-align: center;
  }
  .brand-name span { display: block; font-size: 26px; letter-spacing: 10px; }
  .card--back .brand-name { font-size: 36px; }
  .card--back .brand-name span { font-size: 21px; letter-spacing: 8px; }
  .tagline {
    margin-top: 8px; font-size: 15px; letter-spacing: 1.5px; text-transform: uppercase;
  }
  .card--back .tagline { font-size: 13px; }
  .contact {
    margin-top: 22px; color: var(--slate); text-align: center;
    font-weight: 600; line-height: 1.55; font-size: 15px; letter-spacing: .8px;
  }
  .contact__phone { font-size: 19px; letter-spacing: 2px; }
  .contact__web { font-variant: small-caps; text-transform: lowercase; }
  .contact__address { font-size: 15px; }
  .gold-band {
    position: absolute; left: 0; right: 0; bottom: 0; height: 10px; background: var(--gold);
  }
</style>
</head>
<body>
  <section class="card card--front" aria-label="Card front">
    <div class="brand-mark" aria-hidden="true"></div>
    <h1 class="brand-name">Willowmere<span>Counseling</span></h1>
    <p class="tagline">Endure - Mend - Flourish</p>
  </section>

  <section class="card card--back" aria-label="Card back">
    <div class="brand-mark" aria-hidden="true"></div>
    <h2 class="brand-name">Willowmere<span>Counseling</span></h2>
    <p class="tagline">Endure - Mend - Flourish</p>
    <address class="contact">
      <div class="contact__phone">(214) 555-0187</div>
      <div class="contact__web">www.WillowmereCounseling.example</div>
      <div class="contact__address">3870 N. Garrick Ave., Suite 214, Fort Worth, TX 76132</div>
    </address>
    <div class="gold-band"></div>
  </section>
</body>
</html>
```